Business Card for Business consulting practice

Need a design for a consultant business card. Simple and elegant.
I need the following information on the card:
Logo: (see uploaded file)
Company name: Calmora Advisory Group
Name: Dana Weltrup
Title: Managing Director - Aerospace and Defence
Phone #: 514-268-3917
e-mail: dana.weltrup@calmora-example.com
Website: www.calmora-example.com
Tagline: Proposals Management and Capture support for complex procurements

```html
<!DOCTYPE html>
<html lang="en">
<head>
<meta charset="utf-8">
<title>Calmora Advisory Group – Business Card</title>
<link rel="stylesheet" href="https://fonts.googleapis.com/css2?family=Montserrat:wght@400;500;600&display=swap">
<style>
  :root {
    --page: #f4f4f4;
    --paper: #ffffff;
    --navy: #213849;
    --blue: #1793c0;
  }
  * { margin: 0; padding: 0; box-sizing: border-box; }
  html, body { width: 1200px; height: 1200px; overflow: hidden; background: var(--page); }
  body { position: relative; font-family: "Montserrat", sans-serif; color: var(--navy); }

  .card { position: absolute; left: 225px; width: 754px; height: 430px; overflow: hidden; }
  .card-front { top: 138px; background: var(--paper); }
  .card-back { top: 635px; background: var(--navy); }

  .band { position: absolute; left: 0; bottom: 0; width: 100%; height: 41px; }
  .band-blue { background: var(--blue); }
  .band-navy { left: 590px; width: 164px; background: var(--navy); }

  .brand-disc { position: absolute; left: 0; top: 0; }

  .front-brand { position: absolute; left: 52px; top: 58px; width: 330px; }
  .wordmark { font-weight: 600; white-space: nowrap; }
  .front-brand .wordmark { font-size: 22.5px; color: var(--navy); }
  .tagline { color: var(--blue); font-weight: 600; text-transform: uppercase; white-space: nowrap; }
  .front-brand .tagline { font-size: 6.9px; margin-top: 46px; letter-spacing: 0.1px; }

  .person { position: absolute; left: 52px; top: 176px; }
  .person-name { font-size: 31px; font-weight: 500; letter-spacing: 0.6px; line-height: 1; text-transform: uppercase; }
  .person-name .surname { color: var(--blue); }
  .person-title { font-size: 8px; font-weight: 600; margin-top: 6px; text-transform: uppercase; letter-spacing: 0.3px; }

  .contacts { position: absolute; left: 52px; top: 230px; list-style: none; }
  .contacts li { display: flex; align-items: center; height: 26px; margin-bottom: 5px; font-size: 16px; font-weight: 500; white-space: nowrap; }
  .contacts svg { width: 26px; height: 26px; margin-right: 14px; flex: none; }
  .contacts .phone-number { font-size: 20px; }

  .back-brand { position: absolute; left: 0; right: 0; top: 162px; text-align: center; }
  .back-brand .wordmark { font-size: 37px; color: #ffffff; }
  .back-brand .tagline { font-size: 11.2px; margin-top: 62px; letter-spacing: 0.3px; font-weight: 500; }
</style>
</head>
<body>

<section class="card card-front">
  <div class="band band-blue"></div>
  <div class="band band-navy"></div>
  <svg class="brand-disc" width="754" height="430" viewBox="0 0 754 430" aria-hidden="true">
    <circle cx="592" cy="265" r="164" fill="var(--navy)" stroke="var(--paper)" stroke-width="7"/>
  </svg>

  <div class="front-brand">
    <div class="wordmark">Calmora Advisory Group</div>
    <div class="tagline">Proposals management and capture support for complex procurements</div>
  </div>

  <div class="person">
    <div class="person-name">Dana <span class="surname">Weltrup</span></div>
    <div class="person-title">Managing Director - Aerospace and Defence</div>
  </div>

  <ul class="contacts">
    <li>
      <svg viewBox="0 0 26 26" aria-hidden="true">
        <circle cx="13" cy="13" r="13" fill="var(--blue)"/>
        <path d="M9 6.5c.6-.4 1.3-.2 1.6.4l1.2 2.4c.3.6.1 1.2-.4 1.6l-1 .7c.7 1.8 2 3.2 3.8 4l.8-1c.4-.5 1.1-.6 1.6-.3l2.3 1.3c.6.3.7 1.1.3 1.6l-1 1.2c-.6.7-1.6 1-2.5.7-4-1.3-7-4.4-8.1-8.4-.3-.9 0-1.900.7-2.5z" fill="#fff"/>
      </svg>
      <span class="phone-number">514-268-3917</span>
    </li>
    <li>
      <svg viewBox="0 0 26 26" aria-hidden="true">
        <circle cx="13" cy="13" r="13" fill="var(--blue)"/>
        <rect x="6.5" y="8.5" width="13" height="9" fill="none" stroke="#fff" stroke-width="1.5"/>
        <path d="M6.5 8.5l6.5 5 6.5-5M6.5 17.5l4.8-4.5M19.5 17.5l-4.8-4.5" fill="none" stroke="#fff" stroke-width="1.3"/>
      </svg>
      <span>dana.weltrup@calmora-example.com</span>
    </li>
    <li>
      <svg viewBox="0 0 26 26" aria-hidden="true">
        <circle cx="13" cy="13" r="13" fill="var(--blue)"/>
        <circle cx="13" cy="13" r="7" fill="none" stroke="#fff" stroke-width="1.5"/>
        <path d="M6 13h14M13 6c-2.5 2.5-2.5 11.5 0 14M13 6c2.5 2.5 2.5 11.5 0 14" fill="none" stroke="#fff" stroke-width="1.2"/>
      </svg>
      <span>www.calmora-example.com</span>
    </li>
  </ul>
</section>

<section class="card card-back">
  <div class="back-brand">
    <div class="wordmark">Calmora Advisory Group</div>
    <div class="tagline">Proposals management and capture support for complex procurements</div>
  </div>
</section>

</body>
</html>
```